Skin care manufacturer looking for packaging design for new skin care brand.

We need a design and logo for a skin care brand to be sold at retail stores and online in the United States and Europe. The design will be for 1.7oz - 2oz serums that will not have a retail box. The name of the brand is Orvia Lune and should be a luxurious brand that is approachable. The brand will consist of 4 face serums - Vitamin C, Collagen, Retinol and Hyaluronic Acid that all contain Dead Sea Minerals. Images shown are for inspiration only. Color of bottles can be varied based on design and bottles can be screen printed or labeled.

```html
<!DOCTYPE html>
<html lang="en">
<head>
<meta charset="UTF-8">
<title>Orvia Lune — Serum Labels</title>
<link href="https://fonts.googleapis.com/css2?family=Archivo:wght@700;800;900&family=Montserrat:wght@400;500;700&display=swap" rel="stylesheet">
<style>
  :root {
    --canvas: #ebebeb;
    --label-white: #ffffff;
    --ink: #3a3a3a;
    --ink-soft: #4a4a4a;
    --logo-grey: #7a7a7a;
    --silver-dark: #8d8d8d;
    --silver-light: #e4e4e4;
    --teal-band: #0f6b5c;
    --teal-fade: #3fcab4;
    --orange-band: #e8832b;
    --orange-fade: #ef8a1f;
    --lime-band: #b4c36b;
    --lime-fade: #c3d283;
    --rose-band: #d66f70;
    --rose-fade: #e6898a;
  }
  * { box-sizing: border-box; margin: 0; padding: 0; }
  html, body { width: 1200px; height: 900px; overflow: hidden; }
  body {
    background: var(--canvas);
    font-family: "Montserrat", sans-serif;
    display: flex;
    align-items: center;
    justify-content: center;
  }
  .label-row {
    display: flex;
    gap: 24px;
  }
  .label {
    position: relative;
    width: 270px;
    height: 360px;
    background: linear-gradient(180deg, var(--label-white) 0%, var(--label-white) 32%, var(--fade) 100%);
    display: flex;
    flex-direction: column;
    align-items: center;
    box-shadow: 0 2px 8px rgba(0,0,0,0.08);
  }
  .label--collagen { --band: var(--teal-band); --fade: var(--teal-fade); }
  .label--vitamin-c { --band: var(--orange-band); --fade: var(--orange-fade); }
  .label--hyaluronic { --band: var(--lime-band); --fade: var(--lime-fade); }
  .label--retinol { --band: var(--rose-band); --fade: var(--rose-fade); }

  .brand {
    margin-top: 52px;
    display: flex;
    align-items: center;
    gap: 8px;
    font-family: "Montserrat", sans-serif;
    font-weight: 500;
    font-size: 21px;
    letter-spacing: 1px;
    text-transform: uppercase;
    color: var(--logo-grey);
  }
  .brand__dot {
    width: 8px; height: 8px;
    border-radius: 50%;
    background: var(--logo-grey);
  }
  .product-band {
    margin-top: 50px;
    width: 232px;
    display: flex;
    flex-direction: column;
  }
  .product-band__rule {
    height: 4px;
    background: linear-gradient(90deg, var(--silver-dark), var(--silver-light) 50%, var(--silver-dark));
  }
  .product-band__body {
    background: var(--band);
    height: 80px;
    display: flex;
    flex-direction: column;
    align-items: center;
    justify-content: center;
    color: var(--label-white);
  }
  .product-name {
    font-family: "Archivo", sans-serif;
    font-weight: 900;
    font-size: 32px;
    letter-spacing: 3px;
    line-height: 1;
  }
  .product-name--long {
    font-size: 20px;
    letter-spacing: 0.5px;
  }
  .product-type {
    margin-top: 8px;
    font-size: 12px;
    font-weight: 500;
    letter-spacing: 1px;
    opacity: 0.9;
  }
  .description {
    margin-top: 28px;
    font-size: 12.5px;
    line-height: 1.3;
    letter-spacing: 0.6px;
    text-align: center;
    color: var(--ink-soft);
  }
  .volume {
    margin-top: 30px;
    font-size: 10px;
    font-weight: 700;
    letter-spacing: 1px;
    color: var(--ink);
  }
</style>
</head>
<body>
  <main class="label-row">
    <section class="label label--collagen">
      <div class="brand"><span class="brand__dot"></span>Orvia Lune</div>
      <div class="product-band">
        <div class="product-band__rule"></div>
        <div class="product-band__body">
          <h2 class="product-name">COLLAGEN</h2>
          <p class="product-type">BRIGHTENING SERUM</p>
        </div>
        <div class="product-band__rule"></div>
      </div>
      <p class="description">Lorem Ipsum is simply<br>dummy text of the printing<br>and typesetting industry.</p>
      <p class="volume">50ML/1.7 FLO OZ</p>
    </section>

    <section class="label label--vitamin-c">
      <div class="brand"><span class="brand__dot"></span>Orvia Lune</div>
      <div class="product-band">
        <div class="product-band__rule"></div>
        <div class="product-band__body">
          <h2 class="product-name">VITAMIN C</h2>
          <p class="product-type">BRIGHTENING SERUM</p>
        </div>
        <div class="product-band__rule"></div>
      </div>
      <p class="description">Lorem Ipsum is simply<br>dummy text of the printing<br>and typesetting industry.</p>
      <p class="volume">50ML/1.7 FLO OZ</p>
    </section>

    <section class="label label--hyaluronic">
      <div class="brand"><span class="brand__dot"></span>Orvia Lune</div>
      <div class="product-band">
        <div class="product-band__rule"></div>
        <div class="product-band__body">
          <h2 class="product-name product-name--long">HYALURONIC ACID</h2>
          <p class="product-type">BRIGHTENING SERUM</p>
        </div>
        <div class="product-band__rule"></div>
      </div>
      <p class="description">Lorem Ipsum is simply<br>dummy text of the printing<br>and typesetting industry.</p>
      <p class="volume">50ML/1.7 FLO OZ</p>
    </section>

    <section class="label label--retinol">
      <div class="brand"><span class="brand__dot"></span>Orvia Lune</div>
      <div class="product-band">
        <div class="product-band__rule"></div>
        <div class="product-band__body">
          <h2 class="product-name">RETINOL</h2>
          <p class="product-type">BRIGHTENING SERUM</p>
        </div>
        <div class="product-band__rule"></div>
      </div>
      <p class="description">Lorem Ipsum is simply<br>dummy text of the printing<br>and typesetting industry.</p>
      <p class="volume">50ML/1.7 FLO OZ</p>
    </section>
  </main>
</body>
</html>
```